Brisk Meadow Builders needs a product brochure

We need a new flyer for our Patio Perch Lounge. Here is some of the copy your will need.
"Turn your back yard into the ultimate entertianment venue with the stunning Patio Perch Lounge!"
"Entertain family & friends in your very own back yard!"
"Available with or without solar and comes in a variety of colors"
"The Patio Perch Lounge measures 5' deep by 10' wide and is 9'-6" at it's highest point"
"Constructed with treated 4x4's, primed then painted with Thornby Calder best exterior paint for years of care free enjoyment. Also, Marlow Pendt Keystead shingles are dimensional, have a 25 year warranty and are rated for 150 mph winds!"
"TV Mount included. Shelves and TV are sold separately"
There also needs to be a box where we can add the price into later. The price can change from time to time due to material cost fluctuation.
Look and feel
Each slider illustrates characteristics of the customer's brand and the style your logo design should communicate.

```html
<!DOCTYPE html>
<html lang="en">
<head>
<meta charset="utf-8">
<title>Patio Perch Lounge – Brisk Meadow Builders</title>
<link href="https://fonts.googleapis.com/css2?family=Fredoka:wght@500;600;700&family=Roboto:wght@400;500;700&display=swap" rel="stylesheet">
<style>
  :root {
    --green: #5a9e2f;
    --mint: #e6f1df;
    --orange: #f6ad1b;
    --grey: #4a4a4a;
    --black: #111111;
    --white: #ffffff;
    --canvas: #000000;
    --grass: #86a866;
    --bar: #3d3d3f;
    --paving: #c4c2bd;
  }
  * { margin: 0; padding: 0; box-sizing: border-box; }
  html, body { width: 1200px; height: 1200px; overflow: hidden; background: var(--canvas); }
  .flyer {
    position: absolute; left: 69px; top: 191px; width: 1062px; height: 820px;
    background: var(--white); overflow: hidden;
    font-family: 'Roboto', Arial, sans-serif;
  }
  .abs { position: absolute; }
  .header { left: 0; top: 0; width: 1062px; height: 180px; background: var(--mint); }
  .headline { left: 0; width: 864px; text-align: center; font-family: 'Fredoka', sans-serif; font-weight: 700; white-space: nowrap; }
  .headline.l1 { top: 38px; font-size: 35px; color: var(--grey); letter-spacing: 0.5px; }
  .headline.l1 .rule { display: inline-block; width: 52px; height: 3px; background: var(--green); vertical-align: middle; margin: 0 14px; }
  .headline.l2 { top: 80px; font-size: 34px; color: var(--green); }
  .headline.l3 { top: 118px; font-size: 33px; color: var(--green); }
  .accent { color: var(--orange); }
  .brand { left: 800px; top: 62px; width: 250px; display: flex; align-items: center; gap: 10px; }
  .brand .mark { width: 34px; height: 34px; background: var(--green); flex: none; }
  .brand .name { font-family: 'Fredoka', sans-serif; font-weight: 700; font-size: 25px; line-height: 1.05; color: var(--green); }

  .product-photo { left: 0; top: 250px; }

  .side-column { left: 813px; top: 180px; width: 249px; height: 505px; background: var(--orange); }
  .detail-frame { left: 845px; width: 190px; height: 132px; background: var(--white); border-radius: 8px; padding: 10px; }
  .detail-frame .photo { width: 100%; height: 100%; border: 2px dashed var(--orange); border-radius: 4px; }

  .feature-box {
    top: 214px; height: 102px; border: 3px dashed var(--orange); background: var(--white);
    border-radius: 6px; text-align: center; font-family: 'Fredoka', sans-serif;
    display: flex; flex-direction: column; justify-content: center; box-shadow: 0 0 0 3px #f1f1f1;
  }
  .feature-box .lead { color: var(--green); font-weight: 600; font-size: 15px; line-height: 1.12; }
  .feature-box .note { font-family: 'Roboto', sans-serif; color: var(--black); font-size: 12px; line-height: 1.3; margin-top: 6px; }
  .connector { width: 0; border-left: 3px dotted var(--orange); top: 316px; height: 106px; }

  .specs { left: 377px; top: 220px; width: 430px; list-style: none; font-size: 14px; line-height: 18px; color: var(--black); }
  .specs li { padding-left: 14px; position: relative; }
  .specs li::before { content: ""; position: absolute; left: 0; top: 5px; width: 8px; height: 8px; border-radius: 50%; background: var(--green); }

  .warranty {
    left: 399px; top: 349px; width: 120px; height: 120px; border-radius: 50%; background: var(--orange);
    color: var(--white); text-align: center; font-family: 'Fredoka', sans-serif; font-weight: 700;
    display: flex; flex-direction: column; justify-content: center; border: 4px solid var(--white);
  }
  .warranty .yrs { font-size: 30px; line-height: 1; }
  .warranty .word { font-size: 19px; line-height: 1.1; }
  .sun-rays { left: 520px; top: 346px; }

  .price-box {
    left: 599px; top: 386px; width: 190px; height: 152px; background: var(--black);
    border: 4px solid var(--orange); border-radius: 6px; color: var(--white); text-align: center;
  }
  .price-box .amount { margin-top: 36px; font-weight: 700; font-size: 36px; line-height: 1; }
  .price-box .divider { width: 140px; height: 3px; background: var(--orange); margin: 10px auto 8px; }
  .price-box .alt { font-size: 16px; line-height: 1.35; }
  .price-icon {
    left: 667px; top: 354px; width: 54px; height: 54px; border-radius: 50%; background: var(--green);
    border: 4px solid var(--white); color: var(--white); font-family: 'Fredoka', sans-serif; font-weight: 700;
    font-size: 30px; text-align: center; line-height: 46px;
  }

  .quote-box { left: 585px; top: 550px; width: 228px; height: 135px; background: var(--mint); }
  .quote-box p { position: absolute; left: 0; top: 26px; width: 228px; text-align: center; font-family: 'Fredoka', sans-serif; font-weight: 600; font-size: 18px; line-height: 1.12; color: var(--green); }

  .contact-band { left: 585px; top: 685px; width: 477px; height: 135px; background: var(--green); }
  .phone { left: 585px; top: 696px; width: 477px; text-align: center; font-family: 'Fredoka', sans-serif; font-weight: 700; font-size: 30px; color: var(--orange); display: flex; justify-content: center; align-items: center; gap: 8px; }
  .address { left: 585px; top: 738px; width: 477px; text-align: center; font-weight: 700; font-size: 14px; color: var(--white); }
  .web-pill { left: 659px; top: 770px; width: 340px; height: 50px; background: var(--mint); border-radius: 12px 12px 0 0; text-align: center; line-height: 50px; font-family: 'Fredoka', sans-serif; font-weight: 600; font-size: 27px; color: var(--green); }
  .bottom-strip { left: 0; top: 810px; width: 585px; height: 10px; background: var(--orange); }
</style>
</head>
<body>
<div class="flyer">
  <div class="abs header"></div>
  <div class="abs headline l1"><span class="rule"></span>TURN YOUR BACK YARD INTO<span class="rule"></span></div>
  <div class="abs headline l2">The ULTIMATE Entertainment Venue</div>
  <div class="abs headline l3">with the <span class="accent">STUNNING PATIO PERCH LOUNGE!</span></div>
  <div class="abs brand"><span class="mark"></span><span class="name">BRISK MEADOW BUILDERS</span></div>

  <svg class="abs product-photo" width="585" height="560" viewBox="0 0 585 560" role="img" aria-label="Photo of the Patio Perch Lounge bar with solar panel roof, mounted TV, guests on bar stools, pumpkins and a dog on a paved patio">
    <defs>
      <linearGradient id="photoTone" x1="0" y1="0" x2="0" y2="1">
        <stop offset="0" stop-color="var(--grass)"/>
        <stop offset="0.3" stop-color="#6f7f5e"/>
        <stop offset="0.45" stop-color="var(--bar)"/>
        <stop offset="0.72" stop-color="#55524e"/>
        <stop offset="1" stop-color="var(--paving)"/>
      </linearGradient>
    </defs>
    <path d="M0 190 Q 250 60 585 150 L585 560 L0 560 Z" fill="url(#photoTone)"/>
    <path d="M0 190 Q 250 60 585 150" fill="none" stroke="var(--orange)" stroke-width="4"/>
  </svg>

  <div class="abs side-column"></div>
  <div class="abs detail-frame" style="top:223px"><div class="photo" role="img" aria-label="Photo of bottle shelf mounted on the bar wall" style="background:linear-gradient(#6b5240,#2f2f2f)"></div></div>
  <div class="abs detail-frame" style="top:373px"><div class="photo" role="img" aria-label="Photo of a hand using a bottle opener on the bar post" style="background:linear-gradient(#8a9f7c,#5d4a3a)"></div></div>
  <div class="abs detail-frame" style="top:525px"><div class="photo" role="img" aria-label="Photo of wooden cup holder on the bar counter" style="background:linear-gradient(#3a3a3a,#b07a42)"></div></div>

  <div class="abs feature-box" style="left:36px;width:150px">
    <div class="lead">Available <span class="accent">with</span><br><span class="accent">or without solar</span><br>comes in a<br>variety<br>of colors</div>
  </div>
  <div class="abs feature-box" style="left:204px;width:146px">
    <div class="lead">TV Mount<br>Included</div>
    <div class="note">Shelves and TV<br>are sold separately</div>
  </div>
  <div class="abs connector" style="left:110px"></div>
  <div class="abs connector" style="left:276px"></div>

  <ul class="abs specs">
    <li>DIMENSION: 5' deep x 10' wide x 9'-6" at it's highest point</li>
    <li>Constructed with treated 4x4's,</li>
    <li>Primed then painted with Thornby Calder,<br>best exterior paint for years of care free enjoyment.</li>
    <li>Marlow Pendt Keystead shingles are dimensional</li>
    <li>Rated for 150 mph winds!</li>
  </ul>

  <svg class="abs sun-rays" width="60" height="110" viewBox="0 0 60 110" aria-hidden="true">
    <g stroke="var(--orange)" stroke-width="5" stroke-linecap="round">
      <line x1="8" y1="30" x2="30" y2="10"/>
      <line x1="16" y1="52" x2="48" y2="46"/>
      <line x1="12" y1="74" x2="38" y2="90"/>
    </g>
  </svg>
  <div class="abs warranty"><span class="yrs">25yr</span><span class="word">Warranty</span></div>

  <div class="abs price-box">
    <div class="amount">$99,999</div>
    <div class="divider"></div>
    <div class="alt">With Solar Panel<br>$ 199,999</div>
  </div>
  <div class="abs price-icon">$</div>

  <div class="abs quote-box"><p>"ENTERTAIN FAMILY<br>&amp; FRIENDS IN YOUR<br>VERY OWN<br>BACK YARD!"</p></div>

  <div class="abs contact-band"></div>
  <div class="abs phone">
    <svg width="26" height="26" viewBox="0 0 24 24" aria-hidden="true"><path fill="var(--orange)" d="M6.6 10.8a15.1 15.1 0 0 0 6.6 6.6l2.2-2.2c.3-.3.7-.4 1-.2 1.1.4 2.3.6 3.6.6.6 0 1 .4 1 1V20c0 .6-.4 1-1 1A17 17 0 0 1 3 4c0-.6.4-1 1-1h3.5c.6 0 1 .4 1 1 0 1.3.2 2.5.6 3.6.1.3 0 .7-.2 1z"/></svg>
    04-555-0182
  </div>
  <div class="abs address">2150 Larkfield Rd, Cedar Bend, SC 29000</div>
  <div class="abs web-pill">www.briskmeadow.com</div>
  <div class="abs bottom-strip"></div>
</div>
</body>
</html>
```